Kampagne Stuzzichini
Zielgruppe
Wir Haben ein Restaurant unsere Spezialität ist vorwiegend Italienischer Küche.
Für diese Kampagne wohlen wir hauptsächlich Firmenkunden und Leute duzu bewegen das Sie nach der arbeit, zu uns kommen um einen Apero Zu nehmen ansprechen.
Text:
STUZZICHINI (Überschrift)
Den typischen Apéro aus Italien gibt's Dienstags - Donnerstag ab 17.30 bis 19.00 Uhr zu jedem Getränk Gratis Dazu.
Von Foccacia über Oliven bis zu Lachsbrötchen- lassen Sie sich jede Woche von neuen Leckerbissen aus der Küche der Restaurant Velmo überraschen!
Formate:
Postkarte A6
Volage ist vorhanden
Vorlage mit Verschnitt ist vorhanden.
-Booksmarke 75x210
Vorlage mit verschnitt ist vorhanden.
Ich lade verschiedenen Flyer hoch zur Orientation von style

```html
<!DOCTYPE html>
<html lang="de">
<head>
<meta charset="utf-8">
<title>Restaurant Velmo – Stuzzichini Postkarte</title>
<link rel="stylesheet" href="https://fonts.googleapis.com/css2?family=Abel&family=Oswald:wght@500;600&display=swap">
<style>
  :root {
    --paper: #ffffff;
    --wood-light: #e2d6c4;
    --wood-mid: #d3c2aa;
    --wood-dark: #c4b094;
    --ink: #2b2522;
    --accent: #e8602c;
    --brand: #5b4b3f;
    --rule: #3a3330;
  }
  * { margin: 0; padding: 0; box-sizing: border-box; }
  html, body { width: 1200px; height: 866px; overflow: hidden; background: var(--paper); }
  .postcard { position: relative; width: 1200px; height: 866px; background: var(--paper); font-family: "Abel", sans-serif; color: var(--ink); }

  .wood-panel {
    position: absolute; left: 0; top: 0; width: 572px; height: 866px;
    background: linear-gradient(100deg, var(--wood-light) 0%, var(--wood-mid) 45%, var(--wood-light) 70%, var(--wood-dark) 100%);
  }

  .headline {
    position: absolute; left: 100px; top: 34px;
    font-family: "Oswald", sans-serif; font-weight: 600; font-size: 46px; line-height: 56px;
    letter-spacing: 3px; color: var(--accent); white-space: nowrap;
  }

  .line { position: absolute; left: 100px; white-space: nowrap; }
  .body-line { font-size: 26px; line-height: 32px; }
  .highlight { font-family: "Oswald", sans-serif; font-weight: 600; color: var(--accent); font-size: 40px; line-height: 48px; letter-spacing: 1px; }

  .brand-name { position: absolute; left: 100px; top: 720px; font-size: 36px; line-height: 44px; color: var(--brand); }

  .address-strip {
    position: absolute; left: 580px; top: 42px; width: 22px; height: 784px;
    writing-mode: vertical-rl; transform: rotate(180deg);
    font-family: "Abel", sans-serif; font-size: 15.5px; color: var(--ink);
    display: flex; align-items: center; white-space: nowrap;
  }

  .stamp-box { position: absolute; left: 968px; top: 78px; width: 159px; height: 189px; border: 1.5px solid var(--rule); }

  .address-rule { position: absolute; right: 73px; height: 0; border-top: 1.5px solid var(--rule); }
</style>
</head>
<body>
<div class="postcard">
  <div class="wood-panel" role="img" aria-label="Helle Holzmaserung als Hintergrund"></div>

  <h1 class="headline">STUZZICHINI</h1>

  <p class="line body-line" style="top:118px">Den typischen Apéro aus Italien gibt's</p>
  <p class="line highlight" style="top:173px">Dienstags - Donnerstag</p>
  <p class="line highlight" style="top:238px">ab 17.30 bis 19.00 Uhr</p>
  <p class="line body-line" style="top:304px">zu jedem Getränk Gratis Dazu.</p>
  <p class="line body-line" style="top:361px">Von Foccacia über Oliven bis zu</p>
  <p class="line body-line" style="top:416px">Lachsbrötchen- lassen Sie sich jede</p>
  <p class="line body-line" style="top:473px">Woche von neuen Leckerbissen</p>
  <p class="line body-line" style="top:527px">aus der Küche der Restaurant Velmo</p>
  <p class="line highlight" style="top:567px">überraschen!</p>

  <p class="brand-name">Restaurant Velmo</p>

  <p class="address-strip">Restaurant-Velmo / Lindenweg 12 / 8000 Seewilen / Tel: 044 000 17 30 / info@restaurant-velmo.ch / www.restaurant-velmo.ch</p>

  <div class="stamp-box"></div>

  <div class="address-rule" style="top:494px; left:657px"></div>
  <div class="address-rule" style="top:573px; left:654px"></div>
  <div class="address-rule" style="top:652px; left:647px"></div>
  <div class="address-rule" style="top:732px; left:639px"></div>
</div>
</body>
</html>
```